International oil and gas consultancy needs a business card design

We need a business card design for a new oil and gas consultancy business based in Perth Australia. This is a professional services business and needs a moderately conservative type of business card. The business card also needs to be simple and uncluttered. The colour of the business logo is dark red (see attached file).
The front of the card should have a white background and mainly black lettering and perhaps some use of dark red and/or grey (your choice).
The back of the card should have a light grey background with dark red, black and or both dark red & black lettering (your choice).
Please find attached a clear brief of how I would like the business card designed.

Hello Everyone, I have slightly modified the brief. The main change is to incorporate some dark red and grey colours into the card, while still keeping the black lettering dominant. I have made the changes in the attached detailed brief document. Regards

Please note, the front of the card must say Pelwick Review Services (in addition to the logo).

Conservative

• brief has been updated. please refer to attachment for details.

Front of the card MUST say Pelwick Review Services (in addition to the logo)

```html
<!DOCTYPE html>
<html lang="en">
<head>
<meta charset="utf-8">
<title>Pelwick Review Services – Business Card</title>
<link rel="stylesheet" href="https://fonts.googleapis.com/css2?family=Arimo:wght@400;700&display=swap">
<style>
  :root {
    --brand-red: #9b1b22;
    --ink: #1c1c1c;
    --card-grey: #8a8a8a;
    --card-grey-dark: #727272;
    --paper: #ffffff;
    --ghost: #efe6e3;
    --stage: #e9e7e4;
  }
  * { box-sizing: border-box; margin: 0; padding: 0; }
  html, body { width: 1200px; height: 784px; overflow: hidden; }
  body {
    background: var(--stage);
    font-family: "Arimo", Arial, sans-serif;
    color: var(--ink);
    display: flex;
    align-items: center;
    justify-content: center;
    gap: 48px;
  }
  .card {
    width: 540px;
    height: 320px;
    position: relative;
    overflow: hidden;
    box-shadow: 0 6px 18px rgba(0,0,0,0.18);
  }
  /* Back of card */
  .card-back {
    background: linear-gradient(180deg, var(--card-grey) 0%, var(--card-grey-dark) 100%);
  }
  .card-back .wordmark {
    position: absolute;
    left: 44px;
    top: 104px;
    font-size: 58px;
    font-weight: 700;
    color: var(--brand-red);
    letter-spacing: 2px;
  }
  .services {
    position: absolute;
    left: 330px;
    top: 40px;
    list-style: none;
  }
  .services li {
    color: var(--paper);
    font-size: 14px;
    line-height: 26px;
    display: flex;
    align-items: center;
    gap: 10px;
  }
  .services li::before {
    content: "";
    width: 5px; height: 5px;
    border-radius: 50%;
    background: var(--brand-red);
  }
  .tagline {
    position: absolute;
    left: 44px;
    right: 30px;
    top: 222px;
    font-size: 13px;
    font-weight: 700;
    color: var(--brand-red);
    letter-spacing: 0.6px;
    text-transform: uppercase;
  }
  /* Front of card */
  .card-front { background: var(--paper); }
  .ghost-letter {
    position: absolute;
    right: -20px;
    top: -40px;
    font-size: 420px;
    font-weight: 700;
    line-height: 1;
    color: var(--ghost);
  }
  .card-front .brand {
    position: absolute;
    left: 38px;
    top: 30px;
  }
  .card-front .wordmark {
    font-size: 62px;
    font-weight: 700;
    color: var(--brand-red);
    letter-spacing: 2px;
    line-height: 1;
  }
  .company-name {
    font-size: 17px;
    color: var(--ink);
    margin-top: 6px;
  }
  .person {
    position: absolute;
    left: 38px;
    top: 148px;
  }
  .person .name {
    font-size: 19px;
    font-weight: 700;
    color: var(--brand-red);
  }
  .person .role {
    font-size: 12px;
    line-height: 15px;
  }
  .contacts {
    position: absolute;
    left: 38px;
    top: 208px;
    list-style: none;
  }
  .contacts li {
    display: flex;
    align-items: center;
    gap: 8px;
    font-size: 14px;
    line-height: 19px;
  }
  .contacts svg { width: 13px; height: 13px; flex: none; }
  .contacts .plain { padding-left: 21px; }
</style>
</head>
<body>
  <section class="card card-back" aria-label="Card back">
    <div class="wordmark">PRS</div>
    <ul class="services">
      <li>Joint Venture Audits</li>
      <li>Contract Audits</li>
      <li>Operational Audits</li>
    </ul>
    <p class="tagline">Specialist financial consultants to the oil and gas industry</p>
  </section>

  <section class="card card-front" aria-label="Card front">
    <div class="ghost-letter" aria-hidden="true">P</div>
    <div class="brand">
      <div class="wordmark">PRS</div>
      <div class="company-name">Pelwick Review Services</div>
    </div>
    <div class="person">
      <div class="name">Daniel Marsh</div>
      <div class="role">Director</div>
      <div class="role">Australasia and South East Asia</div>
    </div>
    <ul class="contacts">
      <li>
        <svg viewBox="0 0 16 16" aria-hidden="true"><path d="M8 1 1 7.5h2V15h4v-4h2v4h4V7.5h2z" fill="#9b1b22"/></svg>
        N/A for the business card
      </li>
      <li>
        <svg viewBox="0 0 16 16" aria-hidden="true"><path d="M4 1.5 6.5 5 5 6.5c.8 1.8 2.2 3.3 4.5 4.5L11 9.5l3.5 2.5-1.5 2.5C7 14 2 9 1.5 3z" fill="#9b1b22"/></svg>
        +61 (0)400 318 592
      </li>
      <li>
        <svg viewBox="0 0 16 16" aria-hidden="true"><rect x="1" y="3" width="14" height="10" rx="1" fill="#9b1b22"/><path d="M1.5 4 8 9l6.5-5" stroke="#fff" stroke-width="1.3" fill="none"/></svg>
        daniel@pelwickreview.com
      </li>
      <li>
        <svg viewBox="0 0 16 16" aria-hidden="true"><circle cx="8" cy="8" r="7" fill="#9b1b22"/><path d="M1 8h14M8 1c-3 3.5-3 10.5 0 14M8 1c3 3.5 3 10.5 0 14" stroke="#fff" stroke-width="1" fill="none"/></svg>
        www.pelwickreview.com
      </li>
      <li class="plain">ABN: 51 204 887 036</li>
    </ul>
  </section>
</body>
</html>
```